Tea bag packaging design for KELVIRA

Hello. I am creating a green tea and soybean tea, and I am looking for packaging designs. I will attach some designs I like and our current KELVIRA logo. Feel free to follow the designs or create something of your own.

Package size is 200 (W) x 290(L) mm

The package is a white aluminum package so it can accommodate a wide range of colors. We don't want to pay a ton in printing so 5 colors or less is nice. But we will make exceptions for something more colorful if it's well done.

Target Market(s)

Women and Men in 30s-40s

Industry/Entity Type

food and beverage

Font styles to use
Sans Serif
Other font styles liked:
• red hat is the font of the logo

Requirements
Must have
• clean, simple, but bold design
Nice to have
• images of soybeans and green tea leaves on the package

```html
<!DOCTYPE html>
<html lang="en">
<head>
<meta charset="utf-8">
<title>KELVIRA Organic Tea Range</title>
<link rel="stylesheet" href="https://fonts.googleapis.com/css2?family=Montserrat:wght@500;600;700;800&display=swap">
<style>
  :root {
    --bg: #ffffff;
    --paper: #ececec;
    --paper-shade: #dcdcdc;
    --ink: #111111;
    --red: #ab1530;
    --red-deep: #7b1426;
    --teal: #1ba695;
    --teal-deep: #16806f;
    --orange: #e06d23;
    --orange-deep: #c85a1c;
  }
  * { box-sizing: border-box; margin: 0; padding: 0; }
  html, body {
    width: 1200px; height: 750px; overflow: hidden;
    background: var(--bg);
    font-family: "Montserrat", Arial, sans-serif;
  }
  .range {
    position: relative; width: 1200px; height: 750px;
  }
  .pack {
    position: absolute; top: 181px;
    width: 262px; height: 382px;
    background: linear-gradient(90deg, var(--paper) 0%, #f0f0f0 55%, var(--paper-shade) 100%);
    overflow: hidden;
    border-radius: 2px 2px 4px 4px;
  }
  .pack--red { left: 184px; --accent: var(--red); --accent-deep: var(--red-deep); }
  .pack--teal { left: 496px; --accent: var(--teal); --accent-deep: var(--teal-deep); }
  .pack--orange { left: 804px; --accent: var(--orange); --accent-deep: var(--orange-deep); }

  .pack__pattern {
    position: absolute; left: 0; top: 0; width: 100%; height: 175px;
    background:
      radial-gradient(circle at 25% 30%, var(--accent-deep) 0 16%, transparent 40%),
      radial-gradient(circle at 75% 55%, var(--accent-deep) 0 14%, transparent 38%),
      radial-gradient(circle at 45% 85%, var(--accent-deep) 0 10%, transparent 32%),
      var(--accent);
  }
  .pack__tab {
    position: absolute; left: 50%; top: 130px;
    width: 82px; height: 82px; margin-left: -41px;
    border-radius: 50%;
    background: var(--paper);
  }
  .pack__label {
    position: absolute; left: 0; top: 175px; width: 100%; height: 207px;
    background: linear-gradient(90deg, var(--paper) 0%, #f0f0f0 55%, var(--paper-shade) 100%);
  }
  .brand {
    position: absolute; left: 0; right: 0; top: 183px;
    text-align: center;
    font-weight: 700; font-size: 11px; letter-spacing: 0.2px;
    color: var(--ink);
  }
  .range-title {
    position: absolute; left: 0; right: 0; top: 214px;
    display: flex; align-items: center; justify-content: center; gap: 10px;
    font-weight: 700; font-size: 15px; color: var(--ink);
  }
  .range-title__rule {
    width: 52px; height: 1.2px; background: var(--accent);
  }
  .product-name {
    position: absolute; left: 0; right: 0; top: 233px;
    text-align: center;
    font-weight: 800; font-size: 25px; letter-spacing: -0.3px;
    color: var(--accent);
  }
  .facts {
    position: absolute; left: 31px; top: 289px; width: 192px;
    list-style: none;
    font-weight: 600; font-size: 6.4px; color: var(--ink);
  }
  .facts li {
    padding: 2px 0 3px;
    line-height: 9px;
  }
  .facts li + li { border-top: 1.3px solid var(--accent); padding-top: 4px; }
  .pack__band {
    position: absolute; left: 0; bottom: 0; width: 100%; height: 32px;
  }
  .net-weight {
    position: absolute; left: 0; right: 0; bottom: 11px;
    text-align: center;
    font-weight: 700; font-size: 7.5px; color: #ffffff;
  }
</style>
</head>
<body>
<main class="range">

  <article class="pack pack--red">
    <div class="pack__pattern" role="img" aria-label="Pattern of tea leaves and soybeans in deep red"></div>
    <div class="pack__label"></div>
    <div class="pack__tab"></div>
    <p class="brand">KELVIRA</p>
    <h2 class="range-title"><span class="range-title__rule"></span>ORGANIC<span class="range-title__rule"></span></h2>
    <h1 class="product-name">RED TEA</h1>
    <ul class="facts">
      <li>Origin : SRI LANKA</li>
      <li>Tasting notes: Full Bodied, floral, spicy</li>
      <li>Ingredients: Black loose leaf tea, ginger root</li>
    </ul>
    <svg class="pack__band" viewBox="0 0 262 32" preserveAspectRatio="none" aria-hidden="true">
      <path d="M0 20 Q131 -6 262 14 L262 32 L0 32 Z" fill="var(--accent)"/>
    </svg>
    <p class="net-weight">NET WT : 250g</p>
  </article>

  <article class="pack pack--teal">
    <div class="pack__pattern" role="img" aria-label="Pattern of tea leaves and soybeans in deep teal"></div>
    <div class="pack__label"></div>
    <div class="pack__tab"></div>
    <p class="brand">KELVIRA</p>
    <h2 class="range-title"><span class="range-title__rule"></span>ORGANIC<span class="range-title__rule"></span></h2>
    <h1 class="product-name">MATCHA</h1>
    <ul class="facts">
      <li>Origin : SRI LANKA</li>
      <li>Tasting notes: Full Bodied, floral, spicy</li>
      <li>Ingredients: Black loose leaf tea, ginger root</li>
    </ul>
    <svg class="pack__band" viewBox="0 0 262 32" preserveAspectRatio="none" aria-hidden="true">
      <path d="M0 20 Q131 -6 262 14 L262 32 L0 32 Z" fill="var(--accent)"/>
    </svg>
    <p class="net-weight">NET WT : 250g</p>
  </article>

  <article class="pack pack--orange">
    <div class="pack__pattern" role="img" aria-label="Pattern of tea leaves and soybeans in deep orange"></div>
    <div class="pack__label"></div>
    <div class="pack__tab"></div>
    <p class="brand">KELVIRA</p>
    <h2 class="range-title"><span class="range-title__rule"></span>ORGANIC<span class="range-title__rule"></span></h2>
    <h1 class="product-name">RELAX</h1>
    <ul class="facts">
      <li>Origin : SRI LANKA</li>
      <li>Tasting notes: Full Bodied, floral, spicy</li>
      <li>Ingredients: Black loose leaf tea, ginger root</li>
    </ul>
    <svg class="pack__band" viewBox="0 0 262 32" preserveAspectRatio="none" aria-hidden="true">
      <path d="M0 20 Q131 -6 262 14 L262 32 L0 32 Z" fill="var(--accent)"/>
    </svg>
    <p class="net-weight">NET WT : 250g</p>
  </article>

</main>
</body>
</html>
```